Web Design Project

We need a website design for our marketing agency: clearvane.com.au

We want something that is eye-catching and will wow audiences, yet at the same time it cannot turn-off corporate clients. The website should be highly focused on conversions with numerous call to actions on each page.

We like blue as our primary colour and have a mascot (the spider on the current website)

Target Market(s)

small business owners
small corporations
enterprise level business clients

Industry/Entity Type

Marketing

Requirements
Must have
• must incorporate the agency mascot (the spider on the website)

```html
<!DOCTYPE html>
<html lang="en">
<head>
<meta charset="utf-8">
<title>Clearvane – High ROI Digital Marketing</title>
<link href="https://fonts.googleapis.com/css2?family=Ubuntu:wght@400;500&family=Arimo:wght@400;700&family=EB+Garamond&family=Oswald:wght@500&display=swap" rel="stylesheet">
<style>
:root{
  --blue:#1c5fa8;
  --blue-dark:#0f4f95;
  --nav-top:#1d63ad;
  --nav-bottom:#0d4a8f;
  --hero-top:#2e93d3;
  --hero-bottom:#1a6bb1;
  --sky:#2a86c8;
  --text:#444;
  --muted:#888;
  --grey-band:#d3d3d3;
  --orange:#f7931e;
  --footer:#1458a0;
}
*{margin:0;padding:0;box-sizing:border-box}
html,body{width:1152px;height:1200px;overflow:hidden;background:#fff}
body{position:relative;font-family:"Arimo",Arial,sans-serif;color:var(--text)}
.abs{position:absolute}
a{color:inherit;text-decoration:none}

/* header */
.header{left:0;top:0;width:1152px;height:115px;background:linear-gradient(#fff,#e6e6e6);border-top:3px solid var(--sky)}
.brand{left:128px;top:26px;font-family:"Ubuntu",sans-serif;color:var(--blue);font-size:34px;letter-spacing:1px}
.tagline{left:130px;top:69px;font-family:"Ubuntu",sans-serif;font-size:16px;color:#333}
.mascot{left:328px;top:10px;width:90px;height:95px;border-radius:40% 40% 45% 45%;background:radial-gradient(circle at 50% 50%,#9fb7c9,#5b6e80 70%,transparent 72%)}
.callus{left:762px;top:0;width:258px;height:58px;border-radius:0 0 6px 6px;background:linear-gradient(#2b7cc4,#155da6);border:2px solid #8ab7e0;border-top:0;color:#fff;font-family:"Ubuntu",sans-serif;font-size:22px;display:flex;align-items:center;justify-content:center;gap:6px}
.callus small{font-size:17px}

/* nav */
.nav{left:0;top:115px;width:1152px;height:42px;background:linear-gradient(var(--nav-top),var(--nav-bottom))}
.nav a{position:absolute;top:12px;transform:translateX(-50%);color:#fff;font-size:13.5px;white-space:nowrap}
.nav .active{top:7px;padding:6px 19px;border-radius:4px;background:linear-gradient(#3aa6e8,#1a7fcd)}
.nav .sep{position:absolute;top:10px;width:1px;height:22px;background:#3f7fc0}

/* hero */
.hero{left:0;top:157px;width:1152px;height:335px;background:linear-gradient(var(--hero-top),var(--hero-bottom))}
.arrow{top:135px;width:30px;height:46px}
.quote{left:155px;top:68px;width:430px;font-family:"EB Garamond",serif;font-size:25px;line-height:40px;color:#eef4fb}
.btn-hero{left:155px;top:238px;width:178px;height:44px;border-radius:22px;background:linear-gradient(#fbb040,#f26b1d);color:#fff;font-family:"Oswald",sans-serif;font-size:20px;display:flex;align-items:center;padding-left:28px}
.btn-hero span{position:absolute;right:6px;top:7px;width:30px;height:30px;border-radius:50%;background:#fff;color:#333;font-size:18px;line-height:29px;text-align:center}
.hero-art{left:595px;top:31px;width:375px;height:290px;border-radius:6px;background:linear-gradient(135deg,#f4f7fb,#c9d9ea 55%,#6f9ccd)}

/* welcome */
.welcome{left:118px;top:515px;font-size:31px;color:#333}
.welcome b{font-weight:400;color:var(--blue)}
.intro{left:122px;top:567px;width:620px;font-size:11.5px;line-height:17.3px;text-align:justify}
.intro p+p{margin-top:17px}
.btn-small{background:var(--blue-dark);color:#fff;border-radius:4px;font-size:11.5px;display:flex;align-items:center;justify-content:center}
.vdots{border-left:1px dotted #999}

.testi-head{left:783px;top:514px;width:266px;height:36px;background:var(--blue-dark);color:#fff;font-size:14.5px;padding:10px 8px;box-shadow:0 4px 3px -2px #999}
.testi{left:795px;top:567px;width:246px;font-size:11.5px;line-height:17.3px;color:var(--muted);text-align:justify;text-indent:32px}
.qmark{font-family:"EB Garamond",serif;font-size:50px;color:#ccc;line-height:1}

/* feature columns */
.feature{top:776px;width:280px}
.feature .icon{position:absolute;left:0;top:0;width:48px;height:48px;border-radius:8px}
.feature h3{margin-left:54px;font-weight:400;font-size:17.5px;line-height:21px;color:#333;padding-top:7px}
.feature h3 span{display:block;color:var(--blue)}
.feature p{margin-top:17px;font-size:11.5px;line-height:16px;text-align:justify}
.feature .more{display:block;text-align:right;margin-top:12px;font-size:12px;color:var(--blue)}
.feature .more::before{content:"";display:inline-block;border-left:6px solid #333;border-top:4px solid transparent;border-bottom:4px solid transparent;margin-right:9px}

/* grey band */
.band{left:0;top:946px;width:1152px;height:159px;background:var(--grey-band)}
.panel{top:0;height:159px;overflow:hidden}
.panel.white{background:#fff}
.panel.soft{background:#e4e4e4;border-left:1px solid #bbb;border-right:1px solid #f4f4f4}
.panel .art{position:absolute;width:62px;height:62px;border-radius:50%}
.panel h4{position:absolute;font-weight:400;font-size:18px;line-height:22px;color:#333;white-space:nowrap}
.panel p{position:absolute;font-size:10.5px;line-height:16.3px;text-align:justify}
.panel .go{position:absolute;height:28px;font-size:11px;display:flex;align-items:center;justify-content:center;border-radius:2px}
.go.dark{background:var(--blue-dark);color:#fff}
.go.light{background:#fff;border:1px solid #aaa;color:#333}

/* footer */
.footer{left:0;top:1107px;width:1152px;height:93px;background:var(--footer);color:#fff}
.flinks{left:120px;top:20px;font-size:12px;display:flex;gap:0}
.flinks a:not(:last-child)::after{content:"|";margin:0 11px}
.copy{left:118px;top:48px;font-size:12px;letter-spacing:1px}
.follow{left:890px;top:18px;font-size:12px;color:#bcd2ea;display:flex;align-items:center;gap:6px;letter-spacing:1px}
.follow i{width:22px;height:22px;border-radius:3px;background:#3a8fd6}
</style>
</head>
<body>

<header class="header abs">
  <div class="brand abs">CLEARVANE</div>
  <div class="tagline abs">High Roi Digital Marketing</div>
  <div class="mascot abs" role="img" aria-label="Agency spider mascot illustration"></div>
  <div class="callus abs"><small>CALL US :</small> (+617) 3000 4815</div>
</header>

<nav class="nav abs">
  <a class="active" href="#" style="left:178px">Home</a>
  <span class="sep" style="left:240px"></span>
  <a href="#" style="left:305px">Our Services</a>
  <span class="sep" style="left:384px"></span>
  <a href="#" style="left:431px">Blog</a>
  <span class="sep" style="left:483px"></span>
  <a href="#" style="left:552px">Seo Pricing</a>
  <span class="sep" style="left:626px"></span>
  <a href="#" style="left:673px">SEM</a>
  <span class="sep" style="left:723px"></span>
  <a href="#" style="left:809px">About Clearvane</a>
  <span class="sep" style="left:895px"></span>
  <a href="#" style="left:960px">Contact us</a>
</nav>

<section class="hero abs">
  <svg class="arrow abs" style="left:97px" viewBox="0 0 30 46"><path d="M24 4 L8 23 L24 42" fill="none" stroke="#dfe6ee" stroke-width="7" stroke-linejoin="round"/></svg>
  <svg class="arrow abs" style="left:1043px" viewBox="0 0 30 46"><path d="M6 4 L22 23 L6 42" fill="none" stroke="#eef2f7" stroke-width="7" stroke-linejoin="round"/></svg>
  <blockquote class="quote abs">“…the time has come to ask yourselves does your blog suck … and what are you doing to change it?”</blockquote>
  <a class="btn-hero abs" href="#">READ MORE<span>»</span></a>
  <div class="hero-art abs" role="img" aria-label="Collage of browser windows and online search and social media screens"></div>
</section>

<h1 class="welcome abs" style="font-weight:400">Welcome to <b>CLEARVANE</b></h1>
<div class="intro abs">
  <p>Clearvane is run by Daniel Harrow who resides in Brisbane, Australia. Dan and his specialist team of marketing experts are here to help you build your presence online. We have team members specializing in a range of fields such as: search engine optimisation, social media, online advertising, public relations, general marketing and copywriting. We can even overhaul and optimise your whole website.</p>
  <p>We are an internet marketing consultancy that understands how to effectively combine a diverse array of online marketing techniques to meet your unique needs. We can do much more than just increase your web traffic – we can help you get (and hold onto!) the attention of your target audience and can build your brand online.</p>
</div>
<a class="btn-small abs" href="#" style="left:673px;top:710px;width:70px;height:29px">read more..</a>

<div class="vdots abs" style="left:768px;top:562px;height:168px"></div>
<div class="testi-head abs">Testimonials</div>
<span class="qmark abs" style="left:782px;top:552px">“</span>
<p class="testi abs">Lorem Ipsum is simply dummy text of the printing and typesetting industry. Lorem Ipsum has been the industry's standard dummy text ever since the 1500s, when an unknown printer took a galley of type and scrambled it to make a type specime</p>
<span class="qmark abs" style="left:1003px;top:648px">”</span>
<a class="btn-small abs" href="#" style="left:983px;top:694px;width:57px;height:23px;font-weight:700">more..</a>

<div class="feature abs" style="left:118px">
  <div class="icon" role="img" aria-label="Colourful bar chart icon" style="background:linear-gradient(90deg,#f7931e,#2b7cc4,#8dc63f,#c2272d)"></div>
  <h3>CLEARVANE<span>DIGITAL MARKETING</span></h3>
  <p>Online marketing channels are a major factor almost any business. Clearvane is a digital marketing agency focused on results and ROI. Whether its search engine optimisation with our .....</p>
  <a class="more" href="#">read more...</a>
</div>
<div class="vdots abs" style="left:415px;top:770px;height:148px"></div>
<div class="feature abs" style="left:440px;width:286px">
  <div class="icon" role="img" aria-label="Search engine optimisation puzzle icon" style="background:linear-gradient(135deg,#f2f2f2,#b9c3cc)"></div>
  <h3>SEARCH<span>ENGINE OPTIMISATION</span></h3>
  <p>A website without traffic is useless. Traffic is the commodity of the internet: driving information &amp; business in our online economy. You don't need to have an online store to benefit.....</p>
  <a class="more" href="#">read more...</a>
</div>
<div class="vdots abs" style="left:748px;top:770px;height:148px"></div>
<div class="feature abs" style="left:768px">
  <div class="icon" role="img" aria-label="Rising growth arrows icon" style="background:linear-gradient(135deg,#8dc63f,#2b7cc4 60%,#c2272d)"></div>
  <h3>SEO<span>SERVICES</span></h3>
  <p>It's not just about quantity of traffic but quality. Clearvane's SEO services can drive targeted traffic to your site maximizing your visibility and increasing revenue. .....</p>
  <a class="more" href="#">read more...</a>
</div>

<section class="band abs">
  <div class="panel white abs" style="left:106px;width:310px">
    <div class="art" role="img" aria-label="Computer monitor with globe icon" style="left:12px;top:38px;border-radius:6px;background:linear-gradient(135deg,#dfe9f3,#2b7cc4)"></div>
    <h4 style="left:87px;top:30px">Online Ad Management</h4>
    <p style="left:87px;top:55px;width:200px">Need highly targeted traffic right now? Then let us help! We have a whole range of online advertising solutions , from SearchReach Ads to SocialPost Ads.</p>
    <a class="go dark" href="#" style="left:185px;top:124px;width:97px">Read more...</a>
  </div>
  <div class="panel soft abs" style="left:419px;width:329px">
    <div class="art" role="img" aria-label="Speech bubbles icon" style="left:20px;top:42px;background:radial-gradient(circle at 40% 40%,#8fd0f5,#2b7cc4 55%,#c2272d)"></div>
    <h4 style="left:94px;top:32px">Social Media</h4>
    <p style="left:94px;top:55px;width:206px">Need to engage your target market? Want build your brand to create a loyal base of supporters for your business? Then social media is your solution.</p>
    <a class="go light" href="#" style="left:206px;top:124px;width:92px">Read more...</a>
  </div>
  <div class="panel soft abs" style="left:748px;width:404px;background:#dcdcdc">
    <div class="art" role="img" aria-label="Cardboard package box icon" style="left:26px;top:44px;border-radius:6px;background:linear-gradient(135deg,#e8c47c,#a87a35)"></div>
    <h4 style="left:98px;top:29px">SEO Packages</h4>
    <p style="left:102px;top:55px;width:202px">Drive quality traffic to your business and boost your revenue. We offer high quality SEO packages at competitive rates with GUARANTEED results.</p>
    <a class="go light" href="#" style="left:207px;top:124px;width:91px">Read more...</a>
  </div>
</section>

<footer class="footer abs">
  <div class="flinks abs"><a href="#">Home</a><a href="#">Our Services</a><a href="#">Blog</a><a href="#">Seo Pricing</a><a href="#">SEM</a><a href="#">About Clearvane</a><a href="#">Contact us</a></div>
  <div class="copy abs">Copyright © CLEARVANE 2011 All rights rreserved.</div>
  <div class="follow abs">Follow Us @ <i></i><i></i><i></i></div>
</footer>

</body>
</html>
```